Design Large Inspirational Artwork with Long Quote

Design a large piece of art with a quote from Marcus Hallwell.

QUOTE
"The thing that's so interesting about being alive is that you're all in. No matter what you do, you're all in. This is gonna kill you, so I think you might as well play the most magnificent game you can while you're waiting. Because, do you have anything better to do? Why not pick the best thing possible that you could do? Because you're more powerful than you think, way more powerful than you think. I mean, God only knows what you are in the final analysis. You're blind to your own weaknesses, but you're also blind to your own strengths. How far could you take that if you stopped wasting time, and if you stopped lying, and if you oriented yourself to the highest possible good that you could conceive of and you committed to that? How much good could you do? Well, I would say: why don't you find out?"

SIZE
A high-resolution print size of 6' wide and 3' tall should provide ample space for both the quote and the accompanying artwork.

TYPOGRAPHY
Choose a bold, clean, and easily readable font for the quote. You could also experiment with different font sizes for certain words or phrases to emphasize their importance within the quote.

COLORS
Since the quote is thought-provoking and reflective, you might want to use a color palette that evokes a sense of introspection and depth. Consider using cool, calming colors like shades of blue, gray, or green. Alternatively, you can use a contrasting color scheme with a light background and dark text to make the quote stand out.

ARTWORK
Select / create / edit background artwork to complement the quote.
While a great design might be minimalistic and/or greyscale, I'd really like to see some full color options. This might be anything from photography or graphics inspired by the ideas in the text, to abstract colors or illustrations that feel like the sentiment expressed.
The art should capture your attention and encourage you to read the text. The art should be visually appealing, both at a distance and up close, regardless of whether the text is read.
Updates

Having trouble confirming the exact print size.

Still looking for printing solution and final size confirmation.

Target Market(s)

Personal, business, office

Industry/Entity Type

None

Font styles to use
Sans Serif
Script

Requirements
Must have
• Entire quote, legible text, modern design, attractive artwork, approx 6ft wide and 3ft tall
Nice to have
• Different font (sizes) for certain words or phrases to emphasize their importance within the quote.

```html
<!DOCTYPE html>
<html lang="en">
<head>
<meta charset="utf-8">
<title>Why Don't You Find Out — Quote Artwork</title>
<link rel="stylesheet" href="https://fonts.googleapis.com/css2?family=Jost:wght@300;400;500;600;700&family=Montserrat:wght@900&family=Oswald:wght@500&family=Fredoka:wght@600&family=Sacramento&display=swap">
<style>
  :root {
    --ink: #1b1b1b;
    --sky-top: #cfe1ee;
    --sky-mid: #e7eff5;
    --sky-low: #f6f8fa;
    --blue: #1570b8;
    --orange: #f26522;
    --red: #ed1c24;
    --teal: #15977f;
    --green: #2a9d3c;
    --purple: #8e2c8f;
    --gold: #e8b40a;
    --maroon: #9a1f5e;
    --dot-blue: #2aa5e3;
    --dot-yellow: #ffdf14;
    --dot-green: #3db648;
    --portrait: #3a3a3a;
  }
  * { margin: 0; padding: 0; box-sizing: border-box; }
  html, body { width: 1200px; height: 600px; overflow: hidden; background: #fff; }
  .artwork {
    position: relative;
    width: 1200px;
    height: 600px;
    overflow: hidden;
    font-family: "Jost", sans-serif;
    color: var(--ink);
  }
  .sky-backdrop {
    position: absolute; inset: 0;
    background:
      radial-gradient(ellipse at 15% 30%, rgba(255,255,255,.75), transparent 45%),
      radial-gradient(ellipse at 80% 55%, rgba(255,255,255,.7), transparent 50%),
      radial-gradient(ellipse at 50% 95%, rgba(255,255,255,.9), transparent 55%),
      linear-gradient(180deg, var(--sky-top) 0%, var(--sky-mid) 55%, var(--sky-low) 100%);
  }
  .quote {
    position: absolute; left: 0; top: 0; width: 1170px; height: 600px;
  }
  .line {
    position: absolute; left: 0; width: 100%;
    text-align: center; white-space: nowrap;
    transform: translateY(-50%);
    line-height: 1;
  }
  .script { font-family: "Sacramento", cursive; color: var(--blue); font-size: 46px; vertical-align: -4px; }
  .bold-orange { color: var(--orange); font-weight: 700; }
  .kill { color: var(--red); font-weight: 600; font-style: italic; }
  .teal { color: var(--teal); font-weight: 600; }
  .green { color: var(--green); font-weight: 600; }
  .purple { color: var(--purple); font-weight: 600; }
  .rounded { font-family: "Fredoka", sans-serif; font-weight: 600; }
  .condensed { font-family: "Oswald", sans-serif; font-weight: 500; text-transform: uppercase; letter-spacing: -.3px; }
  .gold { color: var(--gold); }
  .maroon { color: var(--maroon); }
  .red { color: var(--red); }
  .heavy { font-family: "Montserrat", sans-serif; font-weight: 900; letter-spacing: 1px; }
  .attribution {
    position: absolute; right: 231px; top: 498px; transform: translateY(-50%);
    font-family: "Jost", sans-serif; font-weight: 700; font-size: 14px; color: #3a3a3a;
  }
  .accents { position: absolute; inset: 0; }
</style>
</head>
<body>
<main class="artwork">
  <div class="sky-backdrop" role="img" aria-label="Soft blue sky with white clouds"></div>

  <svg class="accents" width="1200" height="600" viewBox="0 0 1200 600">
    <circle cx="1112" cy="347" r="18.5" fill="var(--dot-blue)"/>
    <circle cx="1163" cy="417" r="32.5" fill="var(--dot-yellow)"/>
    <circle cx="1046" cy="475" r="75" fill="var(--dot-green)"/>
    <g role="img" aria-label="Halftone portrait of Marcus Hallwell in a dark suit, arms crossed">
      <path d="M1068 395 Q1090 383 1110 395 L1118 450 Q1150 462 1160 500 L1170 600 L1025 600 L1030 500 Q1040 462 1065 452 Z" fill="var(--portrait)" opacity=".9"/>
    </g>
  </svg>

  <div class="quote">
    <div class="line" style="top:86px;font-size:22px;">The thing that's so interesting about <span class="script">being alive</span> is that you're all in.</div>
    <div class="line" style="top:116px;font-size:26px;">No matter what you do, <span class="bold-orange" style="font-size:32px;">you're all in.</span> This is gonna <span class="kill">kill you,</span></div>
    <div class="line" style="top:151px;font-size:24px;">so I think you might as well play the <span class="teal">most magnificent game</span> you can</div>
    <div class="line" style="top:178px;font-size:22px;">while you're waiting. Because, do you have anything <span class="green">better to do?</span></div>
    <div class="line" style="top:206px;font-size:23px;">Why not pick the <span class="bold-orange">best thing possible</span> that you could do?</div>
    <div class="line" style="top:235px;font-size:26px;font-weight:300;">Because you're more powerful than you think,</div>
    <div class="line heavy" style="top:263px;font-size:28px;">way more powerful than you think.</div>
    <div class="line" style="top:293px;font-size:20px;">I mean, <span class="purple">God only knows</span> what you are in the final analysis.</div>
    <div class="line" style="top:317px;font-size:20px;">You're blind to your own <span class="rounded gold" style="font-size:25px;">weaknesses,</span> but you're also blind to your own <span class="rounded red" style="font-size:25px;">strengths.</span></div>
    <div class="line" style="top:347px;font-size:20px;">How far could you take that if you <span class="condensed gold">stopped wasting time,</span> and if you <span class="condensed gold">stopped lying,</span></div>
    <div class="line" style="top:373px;font-size:20px;">and if you oriented yourself to the <span class="condensed maroon">highest possible good</span> that</div>
    <div class="line" style="top:401px;font-size:20px;">you could <span class="script" style="font-size:44px;">conceive of</span> and you committed to that?</div>
    <div class="line" style="top:428px;font-size:24px;">How much <span class="rounded green" style="font-size:30px;">good</span> could you do?</div>
    <div class="line" style="top:456px;font-size:24px;">Well, I would say: <span class="purple" style="font-size:30px;">why don't you find out?</span></div>
  </div>

  <p class="attribution">Marcus Hallwell.</p>
</main>
</body>
</html>
```